Create a Stationery Design for a start up boutique consultancy in Conflict Management

in starting a boutique consulting business specialising in workplace conflict consulting. That is helping businesses to manage conflict effectively. Some of the services include mediation, workplace investigations, training and facilitation and coaching.
Brannock is usually referred to mediation, negotiation, meetings, etc... The focus is around organisation dialogue.
Seeking logo, letterhead, business card, with comps slip.

Target Market(s)

Corporate HR professionals working in medium to large organisations.

Industry/Entity Type

Boutique

Logo Text

The Brannock Group

Logo styles of interest
Pictorial/Combination Logo
Font styles to use
Sans Serif

Requirements
Must have
• Must have a corporate feel, very professional.
• I want the consultancy to be seen as a premier service.
• Useable format for business cards, websites, etc...

```html
<!DOCTYPE html>
<html lang="en">
<head>
<meta charset="utf-8">
<title>The Brannock Group – Stationery</title>
<link href="https://fonts.googleapis.com/css2?family=Oswald:wght@400&family=Questrial&display=swap" rel="stylesheet">
<style>
:root{
  --backdrop:#d3d3d3;
  --paper:#f2f2f2;
  --ink:#2b2b2b;
  --text:#3a3a3a;
  --gold:#9a7a2c;
  --charcoal:#2e2e2e;
  --charcoal-deep:#262626;
  --silver:#cfcfcf;
  --white:#ffffff;
}
*{margin:0;padding:0;box-sizing:border-box}
html,body{width:1200px;height:1000px;overflow:hidden}
body{background:var(--backdrop);position:relative;font-family:"Questrial",sans-serif;color:var(--text)}
.sheet{position:absolute;background:var(--paper);overflow:hidden}
.wordmark{font-family:"Oswald",sans-serif;font-weight:400;text-transform:uppercase;white-space:nowrap;line-height:1}
.wordmark .mark-square{display:inline-block;background:var(--gold);vertical-align:middle}

/* Decorative footer band placeholder */
.footer-band{position:absolute;left:0;bottom:0;width:100%;
  background:linear-gradient(180deg,var(--paper) 0%,var(--silver) 30%,var(--gold) 50%,var(--charcoal) 100%)}

/* Letterhead */
.letterhead{left:139px;top:82px;width:450px;height:580px}
.letterhead .brand{position:absolute;left:41px;top:64px;font-size:15px;color:var(--ink);display:flex;align-items:center;gap:7px}
.letterhead .brand .mark-square{width:24px;height:24px}
.contact-list{list-style:none;font-size:6px;line-height:7.6px;color:var(--text)}
.contact-list li{display:flex;align-items:center;gap:3px}
.contact-list .icon{width:5px;height:5px;border-radius:1px;background:var(--gold);display:inline-block}
.letterhead .contact-list{position:absolute;left:337px;top:33px}
.letterhead .address{position:absolute;left:337px;top:72px;font-size:6px;line-height:7.6px}
.letterhead .footer-band{height:36px}
.letter-body{position:absolute;left:41px;top:156px;width:370px;font-size:6.1px;line-height:7.3px;text-align:justify}
.letter-body .salutation{font-weight:700;color:var(--ink);margin-bottom:10px}
.letter-body p{margin-bottom:7px}
.sign-off{position:absolute;left:41px;top:352px;font-size:6.1px;line-height:7.5px}
.sign-off strong{color:var(--ink)}
.signature{position:absolute;left:97px;top:354px;width:92px;height:42px;background:linear-gradient(90deg,rgba(70,90,180,.12),rgba(70,90,180,.05));border-radius:3px}

/* Business cards */
.card-front{left:639px;top:82px;width:185px;height:105px}
.card-front .holder{position:absolute;left:11px;top:18px;font-size:6px;font-weight:700;color:var(--ink);letter-spacing:.2px}
.card-front .role{position:absolute;left:11px;top:26px;font-size:4.2px}
.card-front .contact-list{position:absolute;left:11px;top:35px;font-size:4.6px;line-height:5.6px}
.card-front .contact-list .icon{width:4px;height:4px}
.card-front .address{position:absolute;left:11px;top:66px;font-size:4.6px;line-height:5.6px}
.card-front .brand{position:absolute;left:108px;top:22px;font-size:10px;color:var(--ink);line-height:11px}
.card-front .brand .mark-square{width:12px;height:12px;margin-bottom:4px;display:block}
.card-front .footer-band{height:14px}
.card-back{left:874px;top:82px;width:185px;height:105px;background:var(--charcoal)}
.card-back .brand{position:absolute;left:23px;top:24px;font-size:10px;color:var(--white);line-height:11px}
.card-back .brand .mark-square{width:12px;height:12px;margin-bottom:4px;display:block}

/* Presentation folder */
.folder{left:640px;top:238px;width:463px;height:602px;background:linear-gradient(160deg,var(--charcoal),var(--charcoal-deep));border-radius:4px}
.folder .spine{position:absolute;left:27px;top:0;width:2px;height:100%;background:#1f1f1f}
.folder .brand{position:absolute;left:272px;top:66px;font-size:21px;color:var(--white);line-height:26px}
.folder .brand .mark-square{width:32px;height:32px;margin-bottom:10px;display:block}

/* Envelope */
.envelope{left:87px;top:713px;width:501px;height:218px}
.envelope .brand{position:absolute;left:20px;top:44px;font-size:14px;color:var(--ink);display:flex;align-items:center;gap:7px}
.envelope .brand .mark-square{width:20px;height:20px}
.envelope .address{position:absolute;left:45px;top:70px;font-size:6px;line-height:7.6px}
.envelope .footer-band{height:44px}
</style>
</head>
<body>

<section class="sheet letterhead" aria-label="Letterhead">
  <div class="wordmark brand"><span class="mark-square"></span>The Brannock Group</div>
  <ul class="contact-list">
    <li><span class="icon"></span>555-014-2200</li>
    <li><span class="icon"></span>555-014-2201</li>
    <li><span class="icon"></span>info@brannock.com</li>
    <li><span class="icon"></span>www.brannock.com</li>
  </ul>
  <p class="address">4200 Linden Hollow Drive<br>Ashford, Virginia 20170</p>

  <div class="letter-body">
    <p class="salutation">Dear sir,</p>
    <p>Communication is a very integral part of living creatures, animals and humans. Communication may be verbal or written. Written communication however is only applicable to human beings. Can you even imagine a world without communication? Verbal communication can be through telephones, webcams or in person. Written communication is through letters, emails and mobile phone messages.</p>
    <p>In today's world of great inventions and technology, letters have somehow become redundant. It is the time for text messages or chats. But they still can communicate a lot more than all other modes of communication. Organizations and various government departments still bank on letters as a strong medium of communication. There is no comparison in costs of sending letters as compared to costs of mobile phone messages though – letters are far cheaper. Letters now commonly known as "hard copy documents" are considered more relevant and important than email copies of text messages as proof or evidence of some sort.</p>
    <p>Letters speak volumes about a person or an organization that writes it. So one must take utmost care ensuring that the language used in any letter is appropriate for the occasion for which it is being written. Since a letter is also a written proof or document, if there are certain things that should not form a part of it, then that too should be carefully handled.</p>
    <p>Writing a good letter is an art. But if for some reason someone is unable to write that perfect letter, these different types of letters provide a base for you to build on. Sample letters have been given for everyone to understand what all information needs to form a part of the letter type and then it can be customized.</p>
  </div>
  <p class="sign-off">Yours Sincerely,<br><strong>Rowan Ellis</strong></p>
  <div class="signature" role="img" aria-label="Handwritten signature in blue ink"></div>

  <div class="footer-band" role="img" aria-label="Decorative footer band in gold, silver and charcoal"></div>
</section>

<section class="sheet card-front" aria-label="Business card front">
  <p class="holder">MORGAN HALE</p>
  <p class="role">Managing Director</p>
  <ul class="contact-list">
    <li><span class="icon"></span>555-014-2200</li>
    <li><span class="icon"></span>555-014-2201</li>
    <li><span class="icon"></span>info@brannock.com</li>
    <li><span class="icon"></span>www.brannock.com</li>
  </ul>
  <p class="address">4200 Linden Hollow Drive<br>Ashford, Virginia 20170</p>
  <div class="wordmark brand"><span class="mark-square"></span>The<br>Brannock<br>Group</div>
  <div class="footer-band" role="img" aria-label="Decorative footer band in gold, silver and charcoal"></div>
</section>

<section class="sheet card-back" aria-label="Business card back">
  <div class="wordmark brand"><span class="mark-square"></span>The<br>Brannock<br>Group</div>
</section>

<section class="sheet folder" aria-label="Presentation folder">
  <span class="spine"></span>
  <div class="wordmark brand"><span class="mark-square"></span>The<br>Brannock<br>Group</div>
</section>

<section class="sheet envelope" aria-label="Envelope">
  <div class="wordmark brand"><span class="mark-square"></span>The Brannock Group</div>
  <p class="address">4200 Linden Hollow Drive<br>Ashford, Virginia 20170</p>
  <div class="footer-band" role="img" aria-label="Decorative footer band in gold, silver and charcoal"></div>
</section>

</body>
</html>
```